Book Cover Design Book About Commercial Real Estate Investing

I need a book cover designed for my upcoming book.
Need cover for paperback and hardcover book.

The Book is about investing in net lease commercial property.

The book title:

The Steady Yield Manual
Proven Methods For Passive Landlord Buyers
By Mara Colby

Should be minimalist, clean, authoritative, convey money, trust, & growth
I think I like the colors white red and black.
I want a front cover at this time.

Samples I like are included. - the red white and blacks are my favorites

My company is The Corlane Circle
you can learn more about Triple Net Properties at my website
www.TheCorlaneCircle.com

the symbol NNN = Triple net in commercial real estate

Target Market(s)

Affluent male conservative investors

Industry/Entity Type

Real Estate

Requirements
Nice to have
• Sports Motif - - diagrams of sports plays from playbook
• google - Diagrams of sports plays -

```html
<!DOCTYPE html>
<html lang="en">
<head>
<meta charset="utf-8">
<title>The Steady Yield Manual — Mara Colby</title>
<link rel="stylesheet" href="https://fonts.googleapis.com/css2?family=Bebas+Neue&family=Roboto+Condensed:wght@700&family=Montserrat:wght@500&display=swap">
<style>
  :root {
    --paper: #ffffff;
    --paper-edge: #e4e4e4;
    --navy: #233b5d;
    --accent-deep: #cf3f14;
    --accent-light: #f0923f;
    --slate: #7b7b7b;
    --ink: #1c1c1c;
    --photo-tone: #d9d9d9;
  }
  * { margin: 0; padding: 0; box-sizing: border-box; }
  html, body { width: 787px; height: 1200px; overflow: hidden; }
  body { background: var(--paper); }

  .cover {
    position: relative;
    width: 787px;
    height: 1200px;
    overflow: hidden;
    background: radial-gradient(ellipse 80% 65% at 50% 48%, var(--paper) 62%, var(--paper-edge) 100%);
  }

  .title {
    position: absolute;
    top: 22px;
    left: 0;
    width: 100%;
    text-align: center;
    font-family: "Bebas Neue", "Oswald", sans-serif;
    font-weight: 400;
    font-size: 168px;
    line-height: 157px;
    color: var(--navy);
    letter-spacing: 3px;
    white-space: nowrap;
  }
  .title-line { display: block; }
  .title-accent {
    background: linear-gradient(180deg, var(--accent-deep) 15%, var(--accent-light) 85%);
    -webkit-background-clip: text;
    background-clip: text;
    color: transparent;
  }

  .hero-photo {
    position: absolute;
    left: 170px;
    top: 565px;
    width: 460px;
    height: 330px;
    border-radius: 50%;
    background: radial-gradient(ellipse at 45% 45%, var(--photo-tone) 0%, rgba(217,217,217,0.5) 40%, rgba(255,255,255,0) 70%);
  }

  .subtitle {
    position: absolute;
    top: 910px;
    left: 0;
    width: 100%;
    text-align: center;
    font-family: "Roboto Condensed", "Arial Narrow", sans-serif;
    font-weight: 700;
    color: var(--slate);
    text-transform: uppercase;
    white-space: nowrap;
  }
  .subtitle-main { display: block; font-size: 58px; line-height: 64px; }
  .subtitle-joiner { display: block; font-size: 28px; line-height: 32px; }
  .subtitle-tail { display: block; font-size: 52px; line-height: 62px; }

  .author {
    position: absolute;
    top: 1112px;
    left: 0;
    width: 100%;
    text-align: center;
    font-family: "Montserrat", "Helvetica Neue", sans-serif;
    font-weight: 500;
    font-size: 46px;
    line-height: 56px;
    letter-spacing: 8px;
    color: var(--ink);
    text-transform: uppercase;
    white-space: nowrap;
  }
</style>
</head>
<body>
  <main class="cover">
    <h1 class="title">
      <span class="title-line">The <span class="title-accent">Steady</span></span>
      <span class="title-line">Yield</span>
      <span class="title-line">Manual</span>
    </h1>

    <div class="hero-photo" role="img" aria-label="Photo of a pole vaulter in a black singlet launching upward on a bending pole"></div>

    <p class="subtitle">
      <span class="subtitle-main">Proven Methods</span>
      <span class="subtitle-joiner">For</span>
      <span class="subtitle-tail">Passive Landlord Buyers</span>
    </p>

    <p class="author">Mara Colby</p>
  </main>
</body>
</html>
```